KTR Engineering Business Card Design

We’re looking for an elegant, clean, and timeless business card design that communicates experience, capability, and reliability.

KTR Engineering was established in 1995 , we are a Government Contracting company providing Professional Services to the Ministry of Harbor Works, Frontier Stewardship and the Waypoint Consortium. Our capabilities include: Acquisition & Program Management; Intelligence & Security Operations; Cyber, IT & Network Operations; Lifecycle Logistics & Asset Readiness; C5ISR Systems Engineering & Sustainment.

We want the card to reflect a straightforward, confident approach to business. The design should feel polished and professional without being flashy or overly corporate.

Design Direction
Clean, sophisticated, and uncluttered
Elegant but understated
Strong typography and thoughtful spacing
A timeless aesthetic rather than something overly trendy
Confident and established, with a sense of substance
Easy to read and practical in a real-world business setting

The overall impression should be: “These are experienced professionals who know what they’re doing, do what they say, and can be relied upon.”

We’re open to creative interpretations. The finished card should feel distinctive through its typography, proportions, layout, and attention to detail rather than through excessive graphics or visual effects.

We’re looking for a design that would make a potential client immediately feel that they’re dealing with a capable, trustworthy, and established company.

Company Colors: Navy and Gold/Yellow (but you do not need to use these colors on the card)
Company Name: KTR Engineering Associates, Inc. (known as KTR Engineering)
Website: ktrengineering.example
Company Logo: Navy & Gold (other variations attached)

```html
<!DOCTYPE html>
<html lang="en">
<head>
<meta charset="utf-8">
<title>KTR Engineering – Business Card</title>
<link rel="stylesheet" href="https://fonts.googleapis.com/css2?family=Lato:wght@400;700;900&display=swap">
<style>
  :root {
    --backdrop: #8e8e8e;
    --navy: #212a60;
    --navy-deep: #0f1538;
    --gold: #fddf4a;
    --white: #ffffff;
    --olive-dark: #2a2a1c;
  }
  * { margin: 0; padding: 0; box-sizing: border-box; }
  html, body {
    width: 1200px; height: 1000px; overflow: hidden;
    background: var(--backdrop);
    font-family: "Lato", sans-serif;
  }
  .card {
    position: absolute; left: 290px; width: 628px; height: 359px;
    border-radius: 23px; overflow: hidden;
    box-shadow: 0 2px 6px rgba(0,0,0,.25);
  }
  .card--front { top: 97px; background: var(--navy); }
  .card--back {
    top: 532px;
    background: linear-gradient(115deg, var(--navy-deep) 0%, #1b2358 45%, #23263a 70%, var(--olive-dark) 100%);
  }
  .front-visual {
    position: absolute; left: 290px; top: 100px; width: 338px; height: 259px;
    background: radial-gradient(ellipse at 60% 55%, #1a2252 0%, rgba(33,42,96,0) 70%);
  }
  .wordmark {
    position: absolute; color: var(--white); font-weight: 900;
    letter-spacing: -1px; line-height: 1;
  }
  .card--front .wordmark { left: 62px; top: 74px; font-size: 62px; }
  .card--back .wordmark { left: 0; right: 0; top: 148px; text-align: center; font-size: 96px; }
  .holder {
    position: absolute; right: 53px; top: 66px; text-align: right;
  }
  .holder__name { color: var(--gold); font-size: 27px; font-weight: 700; letter-spacing: .3px; line-height: 1; }
  .holder__title { color: var(--white); font-size: 15.5px; margin-top: 7px; }
  .edge-tab { position: absolute; left: 613px; top: 70px; width: 15px; height: 42px; background: var(--white); }
  .company { position: absolute; left: 62px; top: 157px; color: var(--white); font-size: 15.5px; line-height: 21.5px; }
  .company__name { color: var(--gold); font-weight: 700; }
  .contacts { position: absolute; left: 62px; top: 233px; list-style: none; }
  .contacts li {
    display: flex; align-items: center; height: 21.5px;
    color: var(--white); font-size: 15.5px; letter-spacing: .2px;
  }
  .contacts svg { width: 12px; height: 12px; margin-right: 9px; flex: none; }
</style>
</head>
<body>
  <section class="card card--front">
    <div class="front-visual" role="img" aria-label="Faded photograph of a fighter jet in flight, blended into the navy background"></div>
    <div class="wordmark">KTR</div>
    <div class="holder">
      <p class="holder__name">MARLA QUENTON</p>
      <p class="holder__title">President, CEO &amp; Founder</p>
    </div>
    <div class="edge-tab"></div>
    <div class="company">
      <p class="company__name">KTR Engineering Associates, Inc</p>
      <p>4180 Harrow Lane, Suite 310</p>
      <p>Eastport, VA 23400</p>
    </div>
    <ul class="contacts">
      <li><svg viewBox="0 0 12 12"><path d="M2.5 1l2 2-1 1.3c.6 1.4 1.7 2.5 3.2 3.2L8 6.5l2 2-1.2 1.6C5 9.8 2.2 7 1.9 3.2z" fill="var(--gold)"/></svg>555-014-2288</li>
      <li><svg viewBox="0 0 12 12"><rect x="3" y="1" width="6" height="10" rx="1" fill="none" stroke="var(--gold)" stroke-width="1.5"/><circle cx="6" cy="9" r=".8" fill="var(--gold)"/></svg>555-014-2288</li>
      <li><svg viewBox="0 0 12 12"><rect x="1" y="2.5" width="10" height="7" fill="var(--gold)"/><path d="M1 2.5l5 4 5-4" fill="none" stroke="var(--navy)" stroke-width="1"/></svg>info@ktrengineering.example</li>
      <li><svg viewBox="0 0 12 12"><circle cx="6" cy="6" r="5" fill="none" stroke="var(--gold)" stroke-width="1.4"/><path d="M1 6h10M6 1c-2.5 3-2.5 7 0 10M6 1c2.5 3 2.5 7 0 10" fill="none" stroke="var(--gold)" stroke-width="1"/></svg>ktrengineering.example</li>
    </ul>
  </section>

  <section class="card card--back" role="img" aria-label="Dim photograph of an armored vehicle in a hangar with blurred lights, tinted navy">
    <div class="wordmark">KTR</div>
  </section>
</body>
</html>
```